ESTIV Convention 2025 Quebec City

We would like to have a poster for the promotion and publicity of a convention for ESTIV. The goal is to obtain in A4 format and in US letter format (8.5 X 11) a poster for the upcoming convention in Quebec City.
Here are the 2 images (Maren-8 and Maren-24) that we chose yesterday and that inspire us.

Also the 3 posters of previous Conventions (Revue L+E 252, 261 & 273) As a model of what we are looking for.

As for what should also appear on the poster of the Quebec Convention 2025, here are the main points:

Mandatory at the very top of the poster: ESTIV and the wings (as on the posters of the previous Conventions attached) or at least leave such a space free because I believe that the printers of the High Chapter are redoing this acronym by themselves- same for the review Lys-Étoile.
Then the rest can be left to the imagination of the artists.

Here are the important things that should be included:
Harbor Accord
Quebec city
October 11 and 12, 2025
Light (This is the theme of the convention)
Glow to warm every heart (That's the name of the convention)

Please post it in French and NO RELATION TO RELIGIOUS OR RELIGION!!! :)

The website of the organization for more info if required is: www.lys-etoile-demo.org

If you think of anything else to add, no problem.

Target Market(s)

ESTIV members only

Industry/Entity Type

OSBL - Organisme philosophique ( non religieux )

Font styles to use
Serif
Sans Serif

Requirements
Must have
• ESTIV wings logo
Nice to have
• All in French and without reference to religion, also the GOLD color is appreciated
Should not have
• Of aspect or reference to the religious

```html
<!DOCTYPE html>
<html lang="fr">
<head>
<meta charset="utf-8">
<title>ESTIV – Accord du Havre 2025</title>
<link rel="stylesheet" href="https://fonts.googleapis.com/css2?family=Tinos:wght@400;700&display=swap">
<style>
  :root {
    --page: #e9e4dd;
    --deep-blue: #0b3a63;
    --mid-blue: #1278ad;
    --cyan: #39c6ef;
    --glow: #ffffff;
    --pink: #e79ad8;
    --gold: #b88428;
    --gold-bright: #a8741f;
    --gold-dark: #7a531a;
    --brown: #4a2f10;
    --cream: #fbf0c8;
    --cream-edge: #c99a3a;
  }
  * { box-sizing: border-box; margin: 0; padding: 0; }
  html, body { width: 1048px; height: 1200px; overflow: hidden; background: var(--page); }
  body { position: relative; font-family: "Tinos", "Times New Roman", serif; }

  .poster {
    position: absolute; left: 104px; top: 36px;
    width: 840px; height: 1128px; overflow: hidden;
    background: linear-gradient(180deg, #0d4f82 0%, var(--mid-blue) 35%, #15689a 62%, #0e4a72 100%);
  }
  .poster__artwork {
    position: absolute; inset: 0;
    background:
      radial-gradient(ellipse 46% 20% at 50% 18%, var(--glow) 0%, rgba(255,255,255,.85) 35%, rgba(57,198,239,.55) 65%, transparent 100%),
      radial-gradient(ellipse 70% 32% at 50% 20%, rgba(57,198,239,.8) 0%, transparent 80%),
      radial-gradient(ellipse 40% 10% at 35% 38%, rgba(231,154,216,.45) 0%, transparent 100%),
      radial-gradient(circle at 64% 51%, #fff6d6 0%, #f7c77a 6%, #b785c9 13%, rgba(120,90,180,.55) 16%, transparent 22%),
      radial-gradient(ellipse 48% 4% at 50% 86.5%, rgba(255,240,220,.95) 0%, rgba(231,154,216,.5) 50%, transparent 100%),
      linear-gradient(180deg, rgba(11,58,99,.6) 0%, transparent 20%, transparent 80%, rgba(11,58,99,.5) 100%);
  }
  .poster__horizon {
    position: absolute; left: 8%; right: 8%; top: 88.2%; height: 2px;
    background: linear-gradient(90deg, transparent, rgba(255,255,255,.9), transparent);
  }

  .brand {
    position: absolute; left: 50%; top: 17%; transform: translateX(-50%);
    display: flex; align-items: center; gap: 14px;
    color: var(--deep-blue);
    font-weight: 700; font-size: 40px; line-height: 1;
  }
  .brand__dot {
    width: 18px; height: 18px; border-radius: 50%;
    background: var(--deep-blue);
  }

  .title {
    position: absolute; left: 0; right: 0; top: 62.5%;
    text-align: center; color: var(--gold);
    font-weight: 700; font-size: 70px; line-height: 1.02; letter-spacing: -0.5px;
    text-shadow: 2px 3px 0 var(--gold-dark), 0 6px 10px rgba(0,0,0,.35);
  }

  .venue {
    position: absolute; left: 0; right: 0; top: 82%;
    text-align: center; color: var(--gold-bright); font-weight: 700;
  }
  .venue__event { font-size: 34px; line-height: 1.1; }
  .venue__city { font-size: 27px; line-height: 1.2; }

  .date {
    position: absolute; left: 50%; top: 90.6%; transform: translateX(-50%);
    padding: 6px 30px;
    background: linear-gradient(180deg, #fffbe6, var(--cream));
    border: 3px solid var(--cream-edge); border-radius: 30px;
    color: var(--brown); font-weight: 700; font-size: 32px; white-space: nowrap;
  }
</style>
</head>
<body>
  <main class="poster">
    <div class="poster__artwork" role="img" aria-label="Faisceaux de lumière bleue et blanche descendant du ciel étoilé vers un globe terrestre lumineux doré"></div>
    <div class="poster__horizon"></div>

    <header class="brand">
      <span class="brand__dot"></span>
      <span class="brand__name">ESTIV</span>
    </header>

    <h1 class="title">Rayonner pour<br>réchauffer chaque cœur</h1>

    <section class="venue">
      <p class="venue__event">Accord du Havre</p>
      <p class="venue__city">La ville de Québec</p>
    </section>

    <p class="date">11 et 12 octobre 2025</p>
  </main>
</body>
</html>
```